Bref créative
KORVO FREIGHT
BUSINESS CARDS AND BROCHURE LAYOUT
Professional
Reed Quandt
Owner/Specialist
I want no address
korvofreight@nubramail.com
www.korvofreight-example.com
just the logo on the back

```html
<!DOCTYPE html>
<html lang="en">
<head>
<meta charset="utf-8">
<title>Korvo Freight Brochure</title>
<link href="https://fonts.googleapis.com/css2?family=Arimo:wght@400;700&display=swap" rel="stylesheet">
<style>
  :root {
    --red: #c8102e;
    --red-dark: #8e0a1f;
    --grey: #6d6e71;
    --grey-light: #d9d9db;
    --ink: #3a3a3c;
    --white: #ffffff;
    --stage: #ececec;
  }
  * { box-sizing: border-box; margin: 0; padding: 0; }
  html, body { width: 1200px; height: 566px; overflow: hidden; }
  body { background: var(--stage); font-family: "Arimo", Arial, sans-serif; color: var(--ink); position: relative; }
  .spread { position: absolute; top: 48px; height: 470px; display: flex; box-shadow: 0 2px 8px rgba(0,0,0,.18); }
  .spread--outer { left: 150px; }
  .spread--inner { left: 640px; }
  .panel { position: relative; width: 212px; height: 470px; background: var(--white); overflow: hidden; }
  .panel svg.shape { position: absolute; left: 0; width: 212px; display: block; }
  .photo { position: absolute; }
  .photo--truck { left: 0; top: 0; width: 212px; height: 130px; background: linear-gradient(160deg, #cfd6dd, #8a949c 60%, #5b4a3c); }
  .photo--trolley { width: 110px; height: 120px; background: linear-gradient(180deg, #e6d3b5, #b08558 70%, #9a9a9a); border-radius: 4px; }
  .photo--van { right: 10px; top: 12px; width: 90px; height: 50px; background: linear-gradient(180deg, #f4f4f4, #bcc0c4); border-radius: 4px; }
  .photo--parcel { position: absolute; right: 6px; top: 6px; width: 56px; height: 52px; background: linear-gradient(180deg, #d7c09a, #a87f52); }
  .about { position: absolute; left: 0; top: 130px; width: 212px; height: 340px; background: var(--red); padding: 14px 14px; color: var(--white); }
  .tab { display: inline-block; background: var(--red-dark); color: var(--white); font-weight: 700; font-size: 11px; letter-spacing: .5px; padding: 5px 10px; margin-bottom: 10px; }
  .about p { font-size: 8px; line-height: 1.6; margin-bottom: 8px; }
  .brand { position: absolute; left: 0; width: 212px; text-align: center; }
  .brand__name { display: inline-flex; align-items: center; gap: 6px; font-weight: 700; color: var(--red); font-size: 19px; letter-spacing: .3px; white-space: nowrap; }
  .brand__mark { width: 11px; height: 11px; background: var(--red); }
  .brand__tag { font-size: 7px; color: var(--grey); margin-top: 3px; }
  .heading { position: absolute; left: 0; width: 212px; background: var(--red); color: var(--white); font-weight: 700; font-size: 10px; padding: 6px 12px; letter-spacing: .3px; white-space: nowrap; }
  .copy { position: absolute; left: 14px; width: 184px; font-size: 8px; line-height: 1.6; color: var(--ink); }
  .copy p { margin-bottom: 8px; }
  .feature-box { position: absolute; left: 10px; width: 192px; height: 64px; background: var(--red); color: var(--white); font-size: 8px; line-height: 1.5; padding: 8px 70px 8px 8px; }
  .feature-foot { position: absolute; left: 0; bottom: 0; width: 212px; height: 110px; background: var(--red); color: var(--white); font-size: 8px; line-height: 1.6; padding: 22px 14px 0; }
</style>
</head>
<body>

<section class="spread spread--outer">
  <article class="panel panel--about">
    <div class="photo photo--truck" role="img" aria-label="Photo of a delivery worker loading a white truck"></div>
    <div class="about">
      <div class="tab">ABOUT US</div>
      <p>We move parcels and freight across the region with care, speed and clear tracking at every step of the way.</p>
      <p>Our team plans each route so your goods arrive on time and in good shape, whatever the size of the load.</p>
      <p>From small boxes to full pallets, we handle each order as if it were our own. Drivers are trained, vans are clean and every load is insured.</p>
      <p>Call us for a quote and find out how simple shipping can be.</p>
    </div>
  </article>

  <article class="panel panel--cover">
    <svg class="shape" style="top:0" height="140" viewBox="0 0 212 140" aria-hidden="true">
      <path d="M0 0 H212 V70 C150 30 80 50 0 110 Z" fill="var(--red)"/>
      <path d="M0 124 C80 62 150 46 212 84" fill="none" stroke="var(--grey)" stroke-width="4"/>
    </svg>
    <div class="brand" style="top:175px">
      <div class="brand__name"><span class="brand__mark"></span>KORVO FREIGHT</div>
      <div class="brand__tag">freight made simple for you</div>
    </div>
    <div class="photo photo--trolley" style="left:20px; top:290px" role="img" aria-label="Illustration of a hand truck carrying cardboard boxes"></div>
    <svg class="shape" style="bottom:0" height="60" viewBox="0 0 212 60" aria-hidden="true">
      <path d="M0 0 C70 25 140 5 212 30 V60 H0 Z" fill="var(--red)"/>
    </svg>
  </article>
</section>

<section class="spread spread--inner">
  <article class="panel panel--advancement">
    <svg class="shape" style="top:0" height="70" viewBox="0 0 212 70" aria-hidden="true">
      <path d="M0 0 H212 V20 C140 50 70 40 0 60 Z" fill="var(--red)"/>
    </svg>
    <div class="heading" style="top:64px">ADVANCEMENT IN BUSSINESS</div>
    <div class="copy" style="top:98px">
      <p>Steady growth comes from reliable service. We help local shops and large firms ship with less effort and lower cost.</p>
      <p>Flexible pickup times, secure storage and honest rates keep our partners coming back year after year.</p>
      <p>Ask about our business accounts for regular weekly deliveries.</p>
    </div>
    <svg class="shape" style="bottom:0" height="130" viewBox="0 0 212 130" aria-hidden="true">
      <path d="M0 40 C80 0 150 20 212 50 V130 H0 Z" fill="var(--red)"/>
      <path d="M0 30 C80 -8 150 12 212 40" fill="none" stroke="var(--grey)" stroke-width="3"/>
    </svg>
    <div class="brand" style="top:410px">
      <div class="brand__name" style="color:var(--white); font-size:16px"><span class="brand__mark" style="background:var(--white)"></span>KORVO FREIGHT</div>
    </div>
  </article>

  <article class="panel panel--features">
    <svg class="shape" style="top:0" height="90" viewBox="0 0 212 90" aria-hidden="true">
      <path d="M0 0 H212 V40 C140 70 60 50 0 80 Z" fill="var(--grey-light)"/>
      <path d="M0 80 C60 50 140 70 212 40" fill="none" stroke="var(--red)" stroke-width="3"/>
    </svg>
    <div class="photo photo--van" role="img" aria-label="Photo of a white delivery van"></div>
    <div class="heading" style="top:92px; width:auto; left:10px">FEATURES</div>
    <div class="feature-box" style="top:124px">
      Same-day delivery within the city limits, booked online in minutes.
      <div class="photo--parcel" role="img" aria-label="Photo of stacked parcels"></div>
    </div>
    <div class="copy" style="top:200px">
      <p>Live tracking for every parcel, from pickup to the front door, with text alerts on the way.</p>
      <p>Weekend and evening slots are open for homes and offices alike.</p>
    </div>
    <div class="feature-foot">
      Insured loads, trained drivers and friendly support seven days a week. Ask about bulk rates for regular senders.
    </div>
  </article>
</section>

</body>
</html>
```